Lateral thinking Law Firm needs business cards that inspire trust and value

Hi team. After great success with artflockly putting together a sign for us at our local roller-skating rink (yes, we're that cool), we've decided to ask for some designs for our new business cards.

The first card is for Martin Valcourt, Principal, Valcourt Law.
The colours should be blue, white and have some black (no red). Our logo is attached. Please don't use scales of justice, gavels, Court arches, or the blind lady of justice. We find those to cliché.

We want our cards to be eye catching, but classy in line with the legal profession, and showing a depth of character and trust. We are down to earth, highly approachable and modern in approach.

We want our clients to see us as different to the usual stuck up, boring old law firms, but at the same time, to know that we're the strongest, most genuine and dependent part on their team.

Hope that gives you some ideas for our cards. We are based in the Perth Hills (Kelmarton) and our Principal (Martin) has lived in this area for over 40 years.

We love to work with our local community where we can, but do offer services right across the State.

Martin's card should include his mobile number 0417 382 907 and email address martin@valcourtlaw-example.com, plus our website www@valcourtlaw-example.com (which is not yet prepared, but hopefully will be soon!) and mailing address PO Box 817 Kelmarton, WA 6093.

The cards should also include our practice areas - Family Law, Wills and Estates, Building and Construction, Corporate and Commercial, Local Government, Dispute Resolution & Advisory

UPDATE - If designers have the capabilities, please place a QR Code on the back of the card that encodes the business card information as a V-Card.

UPDATE - Please include mailing address PO Box 817 Kelmarton, WA 6093

```html
<!DOCTYPE html>
<html lang="en">
<head>
<meta charset="utf-8">
<title>Valcourt Law – Business Cards</title>
<link rel="stylesheet" href="https://fonts.googleapis.com/css2?family=Montserrat:wght@400;500&display=swap">
<style>
  :root {
    --brand-blue: #4a70b8;
    --paper: #ffffff;
    --backdrop: #2b2c2e;
  }
  * { margin: 0; padding: 0; box-sizing: border-box; }
  html, body {
    width: 1200px; height: 801px; overflow: hidden;
    background: var(--backdrop);
    font-family: "Montserrat", Arial, sans-serif;
  }
  .stage {
    position: relative; width: 1200px; height: 801px;
  }
  .card {
    position: absolute; width: 530px; height: 303px;
    top: 249px; overflow: hidden;
    box-shadow: 0 6px 18px rgba(0,0,0,.45);
  }
  .card--back { left: 50px; background: var(--paper); color: var(--brand-blue); }
  .card--front { left: 620px; background: var(--brand-blue); color: var(--paper); }

  .wordmark {
    font-weight: 500; letter-spacing: 3px; text-transform: uppercase; line-height: 1.05;
  }
  .card--back .wordmark {
    position: absolute; left: 34px; top: 30px; font-size: 30px;
  }
  .card--front .wordmark {
    position: absolute; left: 0; right: 0; top: 100px;
    text-align: center; font-size: 36px;
  }
  .card--front .site {
    position: absolute; left: 0; right: 0; bottom: 34px;
    text-align: center; font-size: 12px; letter-spacing: .3px;
  }

  .contact-list {
    position: absolute; left: 34px; top: 176px; list-style: none;
    font-size: 12.5px; line-height: 19px;
  }
  .contact-list li { display: flex; align-items: center; gap: 8px; }
  .contact-list svg { width: 11px; height: 11px; flex: none; fill: var(--brand-blue); }

  .practice-areas {
    position: absolute; left: 300px; top: 92px; list-style: none;
    font-size: 12.5px; line-height: 19px;
  }
  .practice-areas li { position: relative; padding-left: 13px; }
  .practice-areas li::before {
    content: ""; position: absolute; left: 0; top: 7px;
    width: 5px; height: 5px; border-radius: 50%; background: var(--brand-blue);
  }

  .band-bottom {
    position: absolute; left: 40px; bottom: 0; width: 225px; height: 10px;
    background: var(--brand-blue);
  }
  .band-side {
    position: absolute; right: 0; top: 128px; width: 10px; height: 100px;
    background: var(--brand-blue);
  }
</style>
</head>
<body>
<main class="stage">

  <section class="card card--back" aria-label="Card back">
    <div class="wordmark">Valcourt<br>Law</div>

    <ul class="contact-list">
      <li><svg viewBox="0 0 24 24"><path d="M6.6 10.8a15 15 0 0 0 6.6 6.6l2.2-2.2c.3-.3.7-.4 1-.2 1.1.4 2.3.6 3.6.6.6 0 1 .4 1 1V20c0 .6-.4 1-1 1A17 17 0 0 1 3 4c0-.6.4-1 1-1h3.5c.6 0 1 .4 1 1 0 1.3.2 2.5.6 3.6.1.3 0 .7-.2 1z"/></svg>0417 382 907</li>
      <li><svg viewBox="0 0 24 24"><path d="M2 5h20v14H2zM4 7v.5l8 5 8-5V7l-8 5z"/></svg>martin@valcourtlaw-example.com</li>
      <li><svg viewBox="0 0 24 24"><path d="M12 2a10 10 0 1 0 0 20 10 10 0 0 0 0-20zm0 2c.9 0 2.2 2 2.7 5H9.3C9.8 6 11.1 4 12 4zM4.3 11h3c0 .7 0 1.3.1 2H4.3a8 8 0 0 1 0-2zm.6 4h2.7c.3 1.5.8 2.8 1.4 3.7A8 8 0 0 1 4.9 15zm2.7-6H4.9a8 8 0 0 1 4.1-3.7C8.4 6.2 7.9 7.5 7.6 9zM12 20c-.9 0-2.2-2-2.7-5h5.4c-.5 3-1.8 5-2.7 5zm-2.9-7a17 17 0 0 1 0-2h5.8a17 17 0 0 1 0 2zm5.9 5.7c.6-.9 1.1-2.2 1.4-3.7h2.7a8 8 0 0 1-4.1 3.7zm1.6-5.7c.1-.7.1-1.3.1-2h3a8 8 0 0 1 0 2zm-.2-4c-.3-1.5-.8-2.8-1.4-3.7A8 8 0 0 1 19.1 9z"/></svg>www@valcourtlaw-example.com</li>
      <li><svg viewBox="0 0 24 24"><path d="M12 2a7 7 0 0 0-7 7c0 5 7 13 7 13s7-8 7-13a7 7 0 0 0-7-7zm0 9.5a2.5 2.5 0 1 1 0-5 2.5 2.5 0 0 1 0 5z"/></svg>PO Box 817 Kelmarton, WA 6093</li>
    </ul>

    <ul class="practice-areas">
      <li>Family Law</li>
      <li>Wills and Estates</li>
      <li>Building and Construction</li>
      <li>Corporate and Commercial</li>
      <li>Local Government</li>
      <li>Dispute Resolution &amp; Advisory</li>
    </ul>

    <div class="band-bottom"></div>
    <div class="band-side"></div>
  </section>

  <section class="card card--front" aria-label="Card front">
    <div class="wordmark">Valcourt<br>Law</div>
    <p class="site">www@valcourtlaw-example.com</p>
  </section>

</main>
</body>
</html>
```